Lumen Ridge Puzzles Business Cards
Two-sided business cards
Professional
Pim Varlotte
Founder, KORV Fellow, Brellaquin MVP
pim@lumenridgepuzzles.example
www.lumenridgepuzzles.example
GPG Fingerprint: A2D1 5B09 F6C3 17E4 8D2A 40BC 9E71 3F58 C046
Logo to Use for Business Cards

```html
<!DOCTYPE html>
<html lang="en">
<head>
<meta charset="utf-8">
<title>Lumen Ridge Puzzles Stationery</title>
<link href="https://fonts.googleapis.com/css2?family=Montserrat:wght@400;600;800&display=swap" rel="stylesheet">
<style>
:root{
  --bg:#e9e6e1;
  --blue:#1f4fa8;
  --blue-deep:#0e2f73;
  --sky:#3d8fd6;
  --green:#5c9a2c;
  --green-deep:#2f6418;
  --green-light:#7dbb3f;
  --ink:#1d2d4f;
  --paper:#ffffff;
  --muted:#8c97ab;
  --line:#d7dbe2;
}
*{margin:0;padding:0;box-sizing:border-box}
html,body{width:1200px;height:497px;overflow:hidden;background:var(--bg);font-family:"Montserrat",sans-serif}
.canvas{position:relative;width:1200px;height:497px}
.piece{position:absolute;overflow:hidden;box-shadow:0 2px 6px rgba(0,0,0,.2)}
.piece svg{position:absolute;left:0;top:0}
.brand{display:flex;align-items:center;gap:5px;font-weight:800;color:var(--blue);text-transform:uppercase;letter-spacing:.02em;line-height:1.1;white-space:nowrap}
.brand .dot{width:10px;height:10px;border-radius:50%;background:var(--green);flex:none}
.brand.light{color:#fff}
.brand.light .dot{background:#fff}

/* business cards */
.card{width:190px;height:88px;color:#fff}
.card-front-blue{left:19px;top:70px;background:linear-gradient(110deg,var(--blue-deep) 0 44%,var(--green) 44.5% 100%)}
.card-front-dark{left:216px;top:70px;background:linear-gradient(110deg,#0a1530 0 44%,var(--blue) 44.5% 100%)}
.card-back-blue{left:19px;top:190px;background:linear-gradient(135deg,var(--sky),var(--blue-deep))}
.card-back-green{left:216px;top:190px;background:linear-gradient(135deg,var(--green-light),var(--green-deep))}
.card-web{left:132px;top:307px;width:192px;height:106px;background:var(--paper);color:var(--ink)}

.card-front .brand{position:absolute;left:8px;top:30px;font-size:7px;white-space:normal;width:62px}
.card-front .person{position:absolute;left:98px;top:10px;width:86px;font-size:7px;font-weight:600;line-height:1.2}
.card-front .role{display:block;font-weight:400;font-size:4.2px;margin-top:2px;white-space:nowrap}
.card-front .contact{position:absolute;left:98px;top:44px;width:88px;font-size:4.2px;line-height:1.55;white-space:nowrap}

.card-back .brand{position:absolute;left:0;right:0;top:30px;justify-content:center;font-size:11px}
.card-back .url,.card-web .url{position:absolute;left:0;right:0;bottom:10px;text-align:center;font-size:5px;white-space:nowrap}
.card-web .brand{position:absolute;left:0;right:0;top:38px;justify-content:center;font-size:11px}
.card-web .url{bottom:16px;color:var(--ink)}

/* letterhead */
.letterhead{left:437px;top:29px;width:206px;height:444px;background:var(--paper)}
.letterhead .brand{position:absolute;left:0;right:0;top:36px;justify-content:center;font-size:9px}
.tagline{position:absolute;font-size:4.4px;color:var(--green);letter-spacing:.18em;white-space:nowrap}
.letterhead .tagline{left:0;right:0;top:50px;text-align:center}
.letterhead .contact{position:absolute;left:132px;top:10px;font-size:3.8px;line-height:1.6;color:var(--muted);white-space:nowrap}
.watermark{position:absolute;border-radius:50%;background:rgba(31,79,168,.07)}
.letterhead .watermark{left:68px;top:195px;width:76px;height:76px}

/* envelopes */
.envelope{background:var(--paper)}
.env-back{left:797px;top:34px;width:372px;height:139px}
.env-back .brand{position:absolute;left:0;right:0;top:22px;justify-content:center;font-size:9px}
.env-plain{left:792px;top:115px;width:374px;height:125px}
.env-plain .brand{position:absolute;left:0;right:0;top:28px;justify-content:center;font-size:9px}
.env-front{left:672px;top:211px;width:370px;height:209px}
.env-front .brand{position:absolute;left:26px;top:70px;font-size:11px}
.env-front .tagline{left:42px;top:86px}
.env-front .contact{position:absolute;left:26px;top:150px;font-size:4.2px;line-height:1.6;color:var(--muted);white-space:nowrap}
.env-front .watermark{left:280px;top:120px;width:64px;height:64px}
</style>
</head>
<body>
<main class="canvas">

  <section class="piece card card-front card-front-blue">
    <div class="brand light"><span class="dot"></span>Lumen Ridge Puzzles</div>
    <p class="person">Pim Varlotte<span class="role">Founder, KORV Fellow, Brellaquin MVP</span></p>
    <p class="contact">pim@lumenridgepuzzles.example<br>www.lumenridgepuzzles.example<br>GPG: A2D1 5B09 F6C3 17E4 8D2A<br>40BC 9E71 3F58 C046</p>
  </section>

  <section class="piece card card-front card-front-dark">
    <div class="brand light"><span class="dot"></span>Lumen Ridge Puzzles</div>
    <p class="person">Pim Varlotte<span class="role">Founder, KORV Fellow, Brellaquin MVP</span></p>
    <p class="contact">pim@lumenridgepuzzles.example<br>www.lumenridgepuzzles.example<br>GPG: A2D1 5B09 F6C3 17E4 8D2A<br>40BC 9E71 3F58 C046</p>
  </section>

  <section class="piece card card-back card-back-blue">
    <div class="brand light"><span class="dot"></span>Lumen Ridge</div>
    <p class="url">www.lumenridgepuzzles.example</p>
  </section>

  <section class="piece card card-back card-back-green">
    <div class="brand light"><span class="dot"></span>Lumen Ridge</div>
    <p class="url">www.lumenridgepuzzles.example</p>
  </section>

  <section class="piece card card-web">
    <div class="brand"><span class="dot"></span>Lumen Ridge</div>
    <p class="url">www.lumenridgepuzzles.example</p>
  </section>

  <section class="piece letterhead">
    <svg width="206" height="444" viewBox="0 0 206 444" aria-hidden="true">
      <path d="M0 70 C50 120 40 280 14 444 L0 444 Z" fill="var(--blue)"/>
      <path d="M0 60 C60 120 52 290 30 444 L22 444 C44 290 50 130 0 74 Z" fill="var(--sky)" opacity=".55"/>
      <path d="M0 100 C34 160 28 300 8 444 L0 444 Z" fill="var(--green)"/>
    </svg>
    <div class="brand"><span class="dot"></span>Lumen Ridge Puzzles</div>
    <p class="tagline">PUZZLE STUDIO</p>
    <p class="contact">Pim Varlotte<br>pim@lumenridgepuzzles.example<br>www.lumenridgepuzzles.example</p>
    <div class="watermark"></div>
  </section>

  <section class="piece envelope env-back">
    <svg width="372" height="139" viewBox="0 0 372 139" aria-hidden="true">
      <defs>
        <linearGradient id="flapGreen" x1="0" y1="0" x2="0" y2="1">
          <stop offset="0" stop-color="#7dbb3f"/><stop offset="1" stop-color="#2f6418"/>
        </linearGradient>
      </defs>
      <path d="M0 0 H372 V30 L186 72 L0 30 Z" fill="url(#flapGreen)"/>
    </svg>
    <div class="brand light"><span class="dot"></span>Lumen Ridge</div>
  </section>

  <section class="piece envelope env-plain">
    <svg width="374" height="125" viewBox="0 0 374 125" aria-hidden="true">
      <path d="M0 0 L187 56 L374 0" fill="none" stroke="var(--line)" stroke-width="1"/>
    </svg>
    <div class="brand"><span class="dot"></span>Lumen Ridge</div>
  </section>

  <section class="piece envelope env-front">
    <svg width="370" height="209" viewBox="0 0 370 209" aria-hidden="true">
      <path d="M0 0 H370 V30 C250 62 120 56 0 40 Z" fill="var(--blue)"/>
      <path d="M0 40 C120 56 250 62 370 30 V40 C250 72 120 66 0 50 Z" fill="var(--green)"/>
    </svg>
    <div class="brand"><span class="dot"></span>Lumen Ridge Puzzles</div>
    <p class="tagline">PUZZLE STUDIO</p>
    <p class="contact">Pim Varlotte<br>pim@lumenridgepuzzles.example<br>www.lumenridgepuzzles.example</p>
    <div class="watermark"></div>
  </section>

</main>
</body>
</html>
```